Business letterhead and powerpoint template

Hi, I have recently started using a new logo (found through MarkVesta) and would now like to use that logo for letterheads and powerpoint.

Attached is the logo and one version of a brochure I have recently used.

Business

```html
<!DOCTYPE html>
<html lang="en">
<head>
<meta charset="utf-8">
<title>Halvern Capital Letterhead</title>
<link href="https://fonts.googleapis.com/css2?family=Source+Sans+3:wght@400;600&display=swap" rel="stylesheet">
<style>
  :root {
    --backdrop: #ececec;
    --paper: #ffffff;
    --ink: #222222;
    --ink-soft: #555555;
    --rule: #9a9a9a;
    --accent: #f0703e;
    --accent-pale: #f8dccb;
    --sign-area: #f1f1f1;
  }
  * { margin: 0; padding: 0; box-sizing: border-box; }
  html, body {
    width: 847px; height: 1200px; overflow: hidden;
    background: var(--backdrop);
  }
  body { position: relative; font-family: "Source Sans 3", "Myriad Pro", sans-serif; color: var(--ink); }
  .letterhead {
    position: absolute; left: 102px; top: 196px;
    width: 647px; height: 927px;
    background: var(--paper);
  }
  .brand {
    position: absolute; left: 0; right: 0; top: 50px;
    text-align: center;
    font-size: 32px; font-weight: 400; letter-spacing: 1px;
    color: var(--ink); line-height: 1;
  }
  .brand-rule {
    position: absolute; top: 100px; height: 1px; background: var(--rule);
  }
  .brand-rule.left { left: 28px; width: 290px; }
  .brand-rule.right { left: 330px; width: 292px; }
  .letter-body {
    position: absolute; left: 63px; top: 184px; width: 530px;
    font-size: 13px; line-height: 16.3px;
  }
  .letter-body p { margin-bottom: 15px; }
  .letter-body .gap-large { margin-top: 32px; }
  .signature-area {
    position: absolute; left: 413px; top: 654px; width: 188px; height: 140px;
    background: var(--sign-area); border-radius: 6px;
  }
  .footer-contact {
    position: absolute; left: 0; right: 0; top: 891px;
    text-align: center; font-size: 9.5px; color: var(--ink-soft);
  }
  .footer-contact strong { font-weight: 600; color: var(--ink); }
  .footer-band {
    position: absolute; left: 0; right: 0; bottom: 0; height: 18px;
    background: linear-gradient(90deg, var(--accent-pale) 0%, #f4a27c 55%, var(--accent) 100%);
  }
</style>
</head>
<body>
  <main class="letterhead">
    <div class="brand">HALVERN CAPITAL</div>
    <div class="brand-rule left"></div>
    <div class="brand-rule right"></div>

    <section class="letter-body">
      <p>2250, Cedar Hollow Road<br>Pasadena, CA 91101.</p>
      <p>January 29th, 2011</p>
      <p>Mr. Pellman<br>President, Pellman Youth Center<br>718 Harbor Lane<br>New York, NY 10031</p>
      <p>Dear Mr. Pellman:</p>
      <p>In the first paragraph, one needs to give a brief introduction of oneself. One should also give reference to the purpose of the letter in brief.<br>
      The second paragraph needs to give the details of the letter and its need. This paragraph is mostly longer than the others and plays the main role in the letter. Keep the sentences short and to the point. Avoid using complex words and sentences.</p>
      <p class="gap-large">The third and last paragraph is the conclusion of the letter and can be kept short.</p>
      <p>Sincerely,</p>
      <p>(this is where the signature of the writer will be placed)</p>
      <p>Dana Whitcombe<br>Read more at LetterGuide: http://www.letterguide.example/articles/professional-letter-format.html</p>
    </section>

    <div class="signature-area" role="img" aria-label="Handwritten signature of the sender"></div>

    <footer class="footer-contact">Maple Commerce Tower, 240 King Street, 19th Floor PO Box 311 Toronto, Ontario M5H 3K9 | 1-855-600-4400 | <strong>www.halverncapital.example</strong></footer>
    <div class="footer-band"></div>
  </main>
</body>
</html>
```